Need Landing Page for Data Security Company

Need a new landing page (PSD) for our data security company (www.korvadel.com). We specialize in selling patented hard drive destruction machines that guarantee the data on your hard drives are unrecoverable. We have several large clients such as Lumigrove, Chirpaloo and Vendrix just to name a few. Really want to have a landing page that sticks out.

Attached is a one pager we use just for emailing clients. We do not want the landing page to look like this. This is just for content to read. The landing page needs

Target Market(s)

Government, business corporations, IT decision makers. Not every day user

Industry/Entity Type

It Company

Number of Pages Required

1 page

Font styles to use
Other font styles liked:
• Match Current Website

Requirements
Must have
• Its a landing page so it needs a Contact us Section at the very top!!!
• Need to be a very attractive landing page.. Would like a mix of showcasing our products and also having some client list to show our bigger name clients (lumigrove, vendrix, chirpaloo)
• Landing page needs to use the same color/style schema as current website. Also will be using the same menu structure as what exists today.
• www.korvadel.com
Nice to have
• Maybe some streamvault videos of our products?

```html
<!DOCTYPE html>
<html lang="en">
<head>
<meta charset="utf-8">
<title>Korvadel Innovative Solutions</title>
<link href="https://fonts.googleapis.com/css2?family=Open+Sans:wght@400;600;700&display=swap" rel="stylesheet">
<style>
:root{
  --green:#8cc152;
  --green-dark:#76a943;
  --ink:#2b2b2b;
  --nav:#262626;
  --footer:#1f1f1f;
  --muted:#6f6f6f;
  --line:#e2e2e2;
  --white:#ffffff;
}
*{box-sizing:border-box;margin:0;padding:0}
html,body{width:870px;height:1200px;overflow:hidden}
body{font-family:"Open Sans",Arial,sans-serif;color:var(--ink);background:var(--white);font-size:9px;line-height:1.5}
.wrap{width:720px;margin:0 auto;position:relative}

.top-bar{height:52px;background:var(--white)}
.top-bar .wrap{display:flex;justify-content:space-between;align-items:center;height:52px}
.brand{display:flex;align-items:center;gap:6px;font-size:20px;font-weight:700;color:var(--ink)}
.brand-dot{width:10px;height:10px;border-radius:50%;background:var(--green)}
.contact-strip{display:flex;gap:22px}
.contact-item{display:flex;align-items:center;gap:6px;font-size:8px;color:var(--muted)}
.contact-item svg{width:18px;height:18px}

.main-nav{height:32px;background:var(--nav)}
.main-nav ul{list-style:none;display:flex;justify-content:center;height:32px;align-items:center;gap:4px}
.main-nav a{display:block;padding:0 20px;line-height:32px;color:#ddd;text-decoration:none;font-size:9px}
.main-nav a.active{background:var(--green);color:var(--white)}

.hero{height:258px;position:relative;background:linear-gradient(120deg,#3c3a36 0%,#6d665d 40%,#9a938a 62%,#4a4742 100%)}
.hero-copy{position:absolute;top:96px;left:0;right:0;text-align:center;color:var(--white)}
.hero-copy h1{font-size:24px;font-weight:700}
.hero-copy p{font-size:15px;font-weight:600}

.about{height:354px;background:var(--green);color:var(--white);text-align:center;padding-top:24px}
.about h2{font-size:15px;font-weight:600;margin-bottom:8px}
.about .rule{width:40px;height:2px;background:var(--white);margin:0 auto 14px}
.about p{width:660px;margin:0 auto 10px;font-size:8px;line-height:1.7}
.steps{display:flex;justify-content:center;align-items:flex-start;gap:26px;margin-top:24px}
.step{width:150px}
.step-icon{width:150px;height:76px;background:var(--white);display:flex;align-items:center;justify-content:center;border-radius:3px}
.step-icon svg{width:44px;height:44px}
.step-label{margin-top:8px;font-size:8px}
.step-join{width:26px;height:26px;border-radius:50%;border:2px solid var(--white);margin-top:25px;display:flex;align-items:center;justify-content:center;font-size:14px;font-weight:700}

.videos{padding-top:22px}
.section-head{display:flex;justify-content:space-between;align-items:center;border-bottom:1px solid var(--line);padding-bottom:6px;margin-bottom:16px}
.section-head h3{font-size:9px;font-weight:700;text-transform:uppercase}
.pager{display:flex;gap:3px}
.pager span{width:12px;height:12px;background:var(--line);display:block}
.video-row{display:flex;gap:24px}
.video-card{width:224px}
.video-thumb{height:96px;border-radius:2px}
.thumb-a{background:linear-gradient(135deg,#c9c9c9,#8a8f96)}
.thumb-b{background:linear-gradient(135deg,#d8dcdf,#9aa2a8)}
.thumb-c{background:linear-gradient(135deg,#cfd2d4,#7d8388)}
.video-card h4{font-size:8px;font-weight:700;margin:8px 0 4px}
.video-card p{font-size:7px;color:var(--muted);line-height:1.6}
.video-card .more{font-size:7px;color:var(--green-dark);margin-top:4px;display:block}

.clients{padding-top:18px}
.client-row{display:flex;justify-content:space-between;align-items:center;height:40px}
.client-row span{font-size:12px;font-weight:600;color:#8d8d8d}

.site-footer{position:absolute;top:1030px;left:0;width:870px;height:170px;background:var(--footer);color:#bbb}
.site-footer .wrap{display:flex;padding-top:26px;gap:40px}
.foot-brand{width:200px;text-align:center}
.foot-brand .brand{color:var(--white);justify-content:center;font-size:17px}
.socials{display:flex;justify-content:center;gap:5px;margin-top:10px}
.socials span{width:12px;height:12px;border-radius:50%;background:var(--green)}
.foot-brand small{display:block;font-size:7px;margin-top:12px;color:#888}
.foot-col{width:130px}
.foot-col h5{font-size:8px;color:var(--white);font-weight:700;margin-bottom:8px;text-transform:uppercase}
.foot-col li{list-style:none;font-size:7px;line-height:1.9}
.foot-phone{font-size:18px;color:var(--green);font-weight:700}
</style>
</head>
<body>

<header class="top-bar">
  <div class="wrap">
    <div class="brand"><span class="brand-dot"></span>Korvadel</div>
    <div class="contact-strip">
      <div class="contact-item">
        <svg viewBox="0 0 24 24"><circle cx="12" cy="12" r="11" fill="#8cc152"/><path d="M8 7l2 0 1 3-1.5 1a7 7 0 0 0 3.5 3.5l1-1.5 3 1v2a1 1 0 0 1-1 1A10 10 0 0 1 7 8a1 1 0 0 1 1-1z" fill="#fff"/></svg>
        <span>Call us today<br>555-014-2290</span>
      </div>
      <div class="contact-item">
        <svg viewBox="0 0 24 24"><circle cx="12" cy="12" r="11" fill="#8cc152"/><rect x="6" y="8" width="12" height="8" fill="#fff"/><path d="M6 8l6 5 6-5" stroke="#8cc152" fill="none"/></svg>
        <span>Email us<br>info@korvadel.com</span>
      </div>
    </div>
  </div>
</header>

<nav class="main-nav">
  <ul>
    <li><a class="active" href="#">Home</a></li>
    <li><a href="#">About Us</a></li>
    <li><a href="#">Products</a></li>
    <li><a href="#">Security</a></li>
    <li><a href="#">Compliance</a></li>
    <li><a href="#">Blog</a></li>
    <li><a href="#">Contact</a></li>
  </ul>
</nav>

<section class="hero" role="img" aria-label="Person working on a laptop at a desk with papers">
  <div class="hero-copy">
    <h1>Korvadel Innovative Solutions</h1>
    <p>The Only Hassle Free Automated Crushing System</p>
  </div>
</section>

<section class="about">
  <h2>About Korvadel Technologies</h2>
  <div class="rule"></div>
  <p>Korvadel Technologies is a leader in secure data destruction, building patented machines that physically crush hard drives so that no data can ever be recovered. Our systems are trusted by agencies and enterprises that cannot afford a single leak.</p>
  <p>Every unit is designed for speed, simple operation and full audit trails. Drives are logged, crushed and verified in seconds, giving IT decision makers proof of destruction for compliance reviews. Our team supports each install with training, service and clear documentation so your staff can work with confidence from day one.</p>
  <div class="steps">
    <div class="step">
      <div class="step-icon"><svg viewBox="0 0 44 44"><rect x="8" y="10" width="28" height="24" rx="3" fill="none" stroke="#8cc152" stroke-width="3"/><circle cx="22" cy="22" r="5" fill="#8cc152"/></svg></div>
      <div class="step-label">Insert the hard drive</div>
    </div>
    <div class="step-join">+</div>
    <div class="step">
      <div class="step-icon"><svg viewBox="0 0 44 44"><rect x="10" y="6" width="24" height="32" rx="2" fill="none" stroke="#8cc152" stroke-width="3"/><path d="M16 22h12M22 16v12" stroke="#8cc152" stroke-width="3"/></svg></div>
      <div class="step-label">Press to crush automatically</div>
    </div>
    <div class="step-join">+</div>
    <div class="step">
      <div class="step-icon"><svg viewBox="0 0 44 44"><circle cx="22" cy="22" r="15" fill="none" stroke="#8cc152" stroke-width="3"/><path d="M14 22l6 6 11-12" stroke="#8cc152" stroke-width="3" fill="none"/></svg></div>
      <div class="step-label">Data is destroyed and verified forever</div>
    </div>
  </div>
</section>

<section class="videos">
  <div class="wrap">
    <div class="section-head"><h3>Product Video</h3><div class="pager"><span></span><span></span></div></div>
    <div class="video-row">
      <article class="video-card">
        <div class="video-thumb thumb-a" role="img" aria-label="Video still of a drive crushing machine"></div>
        <h4>DataCrush</h4>
        <p>Watch the compact crusher punch through a full drive in under ten seconds with zero setup.</p>
        <span class="more">Watch now</span>
      </article>
      <article class="video-card">
        <div class="video-thumb thumb-b" role="img" aria-label="Video still of a crushed hard drive"></div>
        <h4>DataCrush Compact</h4>
        <p>See how the desktop model fits any office and logs each drive for a full audit trail.</p>
        <span class="more">Watch now</span>
      </article>
      <article class="video-card">
        <div class="video-thumb thumb-c" role="img" aria-label="Video still of an industrial destruction unit"></div>
        <h4>DataCrush Pro</h4>
        <p>Our heavy duty unit handles high volumes for data centers and government sites.</p>
        <span class="more">Watch now</span>
      </article>
    </div>
  </div>
</section>

<section class="clients">
  <div class="wrap">
    <div class="section-head"><h3>Our Clients</h3><div class="pager"><span></span><span></span></div></div>
    <div class="client-row">
      <span>Lumigrove</span><span>Chirpaloo</span><span>Vendrix</span><span>Orbanet</span><span>Teskora</span><span>Hallowmere</span>
    </div>
  </div>
</section>

<footer class="site-footer">
  <div class="wrap">
    <div class="foot-brand">
      <div class="brand"><span class="brand-dot"></span>Korvadel</div>
      <div class="socials"><span></span><span></span><span></span><span></span></div>
      <small>© Korvadel Technologies</small>
    </div>
    <div class="foot-col">
      <h5>Services</h5>
      <ul><li>Drive Destruction</li><li>On Site Service</li><li>Audit Reports</li><li>Training</li><li>Support</li></ul>
    </div>
    <div class="foot-col">
      <h5>Products</h5>
      <ul><li>DataCrush</li><li>DataCrush Compact</li><li>DataCrush Pro</li><li>Degaussers</li><li>Accessories</li></ul>
    </div>
    <div class="foot-col">
      <h5>Contact Us</h5>
      <div class="foot-phone">555-014-2290</div>
      <ul><li>info@korvadel.com</li></ul>
    </div>
  </div>
</footer>

</body>
</html>
```